KV Group

We need a new website for our company and since we had a very good work done for our logo in this site, we're back for the entire job.

Our company name is Marlowe Capital Group. We're adding files of examples of what we have done today. In my opinion we need a more attention lock in the site but yet financial simple work.

Our files (attached) will let you know what we have so far. We need a complete change but the colours should be the same, however you can change them not running away to far from the original, and of course matching with the logo.

We need examples for 3 kind of layouts.

- A HOME welcome layout
- An internal Layout with sidebar
- And internal Layout wide

We can buy image licenses if needed for assets.
Actually there are 5 slide images placed on the Welcome HOME, we need those there, but you can improve with better images to match the new website!!!

Target Market(s)

Clients looking for financial advisers, tax and funds specialist, currency advisers

Industry/Entity Type

Financial

Requirements
Must have
• all the fonts must be in accordance with the financial market sites........the welcome home page must be precise, neat and information accurate........the menu should be elegant........main focus on the Home page, should be also the PRIVATE ACCESS box log in.......

```html
<!DOCTYPE html>
<html lang="fr">
<head>
<meta charset="utf-8">
<title>Marlowe Capital Group</title>
<link href="https://fonts.googleapis.com/css2?family=Open+Sans:ital,wght@0,400;0,600;0,700;1,400&family=Courier+Prime:wght@700&display=swap" rel="stylesheet">
<style>
:root{
  --orange:#f47b20;
  --dark:#222222;
  --ink:#333333;
  --muted:#888888;
  --rule:#e2e2e2;
  --white:#ffffff;
  --up:#1c8a1c;
  --down:#d01818;
  --navy:#1a2a5a;
  --seal:#c9c9c9;
}
*{margin:0;padding:0;box-sizing:border-box}
html,body{width:874px;height:1200px;overflow:hidden;background:var(--white)}
body{position:relative;font-family:"Open Sans",Arial,sans-serif;color:var(--ink)}
a{color:inherit;text-decoration:none}
.abs{position:absolute}

.topbar{left:0;top:0;width:874px;height:7px;background:var(--dark)}
.top-btn{top:8px;height:21px;background:var(--dark);color:var(--white);font-size:9.5px;display:flex;align-items:center;justify-content:center;gap:5px;border-radius:0 0 2px 2px}
.apply{left:618px;width:84px}
.contact{left:710px;width:84px}
.social{top:44px;width:16px;height:16px;background:var(--orange)}
.search{left:618px;top:70px;width:176px;height:30px;border:1px solid var(--rule);border-radius:2px;font-size:7px;font-style:italic;color:var(--muted);padding:0 0 0 13px;display:flex;align-items:center}
.search svg{position:absolute;right:9px;top:8px}

.brand-mark{left:124px;top:36px;width:22px;height:22px;background:var(--orange)}
.brand-name{left:81px;top:82px;font-size:11.5px;font-weight:600;letter-spacing:.3px;color:var(--dark);white-space:nowrap}
.brand-line{left:81px;top:97px;width:137px;height:1px;background:var(--dark)}

.nav{left:81px;top:123px;height:45px;display:flex;align-items:center;font-size:11.3px;color:var(--dark)}
.nav a{padding:0 20px;border-left:1px solid #999;line-height:12px}
.nav a:nth-child(2){border-left:none}
.nav .home{background:var(--orange);color:var(--white);height:45px;display:flex;align-items:center;padding:0 11px;border:none;margin-right:5px}

.hero{left:81px;top:185px;width:713px;height:264px;background:
  radial-gradient(ellipse 300px 200px at 600px 40px,#f4f1c0 0%,#d7d6a0 30%,transparent 75%),
  linear-gradient(90deg,#4c6b6e 0%,#6e8a83 35%,#a9b28e 65%,#cfc992 100%)}
.hero-title{left:99px;top:220px;font-size:18px;font-weight:600;color:var(--orange)}
.hero-rule{left:99px;top:254px;width:187px;height:1px;background:rgba(255,255,255,.35)}
.lbl{left:99px;font-size:10px;color:var(--white)}
.field{left:99px;width:185px;height:27px;background:var(--white);font-size:6.8px;font-style:italic;color:#999;padding-left:8px;display:flex;align-items:center}
.forgot{left:99px;top:391px;font-size:7.5px;color:var(--white);text-decoration:underline}
.login{left:203px;top:386px;width:83px;height:21px;background:var(--orange);color:var(--white);font-size:8.6px;font-weight:700;display:flex;align-items:center;justify-content:center}

.sec-title{left:81px;font-size:19px;font-weight:600;color:var(--orange);white-space:nowrap}
.sec-rule{height:4px;border-top:1px solid var(--rule);border-bottom:1px solid var(--rule);right:80px}

.feat-icon{top:518px;width:31px;height:29px;background:var(--dark)}
.feat-icon svg{position:absolute;left:8px;top:7px}
.feat-name{top:522px;font-size:13px;font-weight:600;color:var(--dark)}
.feat-text{top:558px;width:210px;font-size:8.4px;line-height:11px;color:var(--ink)}
.read{top:601px;font-size:8.6px;color:var(--orange);text-decoration:underline}

.welcome{left:81px;width:714px;font-size:8.9px;line-height:14px;color:var(--ink)}

.ticker{left:82px;top:820px;width:714px;height:42px;background:#f6f6f6;border:1px solid #ececec;overflow:hidden}
.ticker-row{position:absolute;left:1px;top:18px;white-space:nowrap;font-family:"Courier Prime","Courier New",monospace;font-weight:700;font-size:7.5px;color:var(--navy)}
.ticker-row span{margin-right:18px}
.up{color:var(--up)}.down{color:var(--down)}.flat{color:#e4a020}

.verified{left:83px;top:893px;font-size:11.5px;font-weight:600;color:var(--dark)}
.badge{top:918px}

.footer{left:82px;top:989px;width:714px;height:211px;background:var(--dark)}
.footer-bottom{left:82px;top:1172px;width:714px;height:28px;background:#1c1c1c;border-top:1px solid #2e2e2e;color:#aaa;font-size:7px;display:flex;align-items:center;justify-content:center}
.fcol{top:1002px}
.fcol h4{font-size:12px;font-weight:600;color:var(--white);margin-bottom:7px}
.fcol li{list-style:none;font-size:8.4px;line-height:13.1px;color:#8e8e8e}
</style>
</head>
<body>
<div class="abs topbar"></div>
<a class="abs top-btn apply" href="#"><svg width="9" height="10" viewBox="0 0 9 10"><rect x="1" y="0.5" width="6" height="8" fill="none" stroke="#fff"/><rect x="3" y="2.5" width="5.5" height="7" fill="#fff"/></svg>APPLY NOW</a>
<a class="abs top-btn contact" href="#"><svg width="9" height="9" viewBox="0 0 9 9"><path d="M1 2 Q1 8 7 8 L8 6.5 L6 5.5 L5 6.5 Q2.5 5.5 2.5 4 L3.5 3 L2.5 1 Z" fill="#fff"/></svg>CONTACT US</a>
<div class="abs social" style="left:720px"></div>
<div class="abs social" style="left:749px"></div>
<div class="abs social" style="left:778px"></div>
<div class="abs search">Enter your search here<svg width="12" height="12" viewBox="0 0 12 12"><circle cx="5" cy="5" r="3.8" fill="none" stroke="#222" stroke-width="1.6"/><path d="M8 8 L11 11" stroke="#222" stroke-width="1.8"/></svg></div>

<div class="abs brand-mark"></div>
<div class="abs brand-name">MARLOWE CAPITAL</div>
<div class="abs brand-line"></div>

<nav class="abs nav">
  <a class="home" href="#">Home</a>
  <a href="#">About Us</a>
  <a href="#">Investments</a>
  <a href="#">Funds</a>
  <a href="#">Brokerage</a>
  <a href="#">Exchange</a>
  <a href="#">Accounts</a>
</nav>

<div class="abs hero" role="img" aria-label="Photo: two hands joining puzzle pieces against a bright hazy sky"></div>
<div class="abs hero-title">PRIVATE ACESS</div>
<div class="abs hero-rule"></div>
<div class="abs lbl" style="top:268px">Account Number</div>
<div class="abs field" style="top:290px">Please your account number</div>
<div class="abs lbl" style="top:326px">Account Password</div>
<div class="abs field" style="top:347px">Please your account password</div>
<a class="abs forgot" href="#">Forgot Acc No. / Password ?</a>
<a class="abs login" href="#">Log into Account</a>

<h2 class="abs sec-title" style="top:472px">Our Features</h2>
<div class="abs sec-rule" style="left:213px;top:484px"></div>

<div class="abs feat-icon" style="left:81px"><svg width="15" height="15" viewBox="0 0 15 15"><path d="M1 14 H14 M2 12 L12 2 M7 2 H12 V7" stroke="#f47b20" stroke-width="2" fill="none"/></svg></div>
<div class="abs feat-name" style="left:121px">Management &amp; Strategy</div>
<p class="abs feat-text" style="left:81px">Contrairement à une opinion répandue, le Lorem Ipsum n'est pas simplement du texte aléatoire. Il trouve ses racines dans.</p>
<a class="abs read" style="left:81px" href="#">Read More</a>

<div class="abs feat-icon" style="left:334px"><svg width="15" height="15" viewBox="0 0 15 15"><rect x="1" y="1" width="13" height="13" fill="none" stroke="#f47b20" stroke-width="1.6"/><path d="M10 4 H6 V7.5 H9.5 V11 H5" stroke="#f47b20" stroke-width="1.6" fill="none"/></svg></div>
<div class="abs feat-name" style="left:374px">Fund</div>
<p class="abs feat-text" style="left:334px">Contrairement à une opinion répandue, le Lorem Ipsum n'est pas simplement du texte aléatoire. Il trouve ses racines dans.</p>
<a class="abs read" style="left:334px" href="#">Read More</a>

<div class="abs feat-icon" style="left:584px"><svg width="15" height="15" viewBox="0 0 15 15"><path d="M2 7 A5.5 5.5 0 0 1 12 4.5 M13 8 A5.5 5.5 0 0 1 3 10.5" stroke="#f47b20" stroke-width="2" fill="none"/><path d="M9.5 4.5 H13 V1 M5.5 10.5 H2 V14" stroke="#f47b20" stroke-width="2" fill="none"/></svg></div>
<div class="abs feat-name" style="left:625px">Currency Exchange</div>
<p class="abs feat-text" style="left:584px">Contrairement à une opinion répandue, le Lorem Ipsum n'est pas simplement du texte aléatoire. Il trouve ses racines dans.</p>
<a class="abs read" style="left:584px" href="#">Read More</a>

<h2 class="abs sec-title" style="top:650px">Welcome to Marlowe Capital Group</h2>
<div class="abs sec-rule" style="left:424px;top:662px"></div>
<p class="abs welcome" style="top:686px">Le Lorem Ipsum est simplement du faux texte employé dans la composition et la mise en page avant impression. Le Lorem Ipsum est le faux texte standard de l'imprimerie depuis les années 1500.</p>
<p class="abs welcome" style="top:727px">Quand un peintre anonyme assembla ensemble des morceaux de texte pour réaliser un livre spécimen de polices de texte. Il n'a pas fait que survivre cinq siècles, mais s'est aussi adapté à la bureautique informatique, sans que son contenu n'en soit modifié. Il a été popularisé dans les années 1960 grâce à la vente de feuilles.On sait depuis longtemps que travailler avec du texte lisible et contenant du sens est source de distractions, et empêche de se concentrer sur la mise en page elle-même.L'avantage du Lorem Ipsum sur un texte générique comme 'Du texte. Du texte.' est qu'il possède une distribution</p>

<div class="abs ticker">
  <div class="ticker-row">
    <span>GBP/UAH = <b class="up">12.65761 ▲</b></span>
    <span>GBP/UGX = <b class="down">4010.06174 ▼</b></span>
    <span>GBP/USD = <b class="up">1.55817 ▲</b></span>
    <span>GBP/UYU = <b class="up">34.36026 ▲</b></span>
    <span>GBP/VEF = <b class="flat">0</b></span>
    <span>GBP/VUV = <b class="up">151</b></span>
    <span>GBP/UAH = <b class="up">12.65761 ▲</b></span>
  </div>
</div>

<div class="abs verified">Verified &amp; Protected by</div>
<svg class="abs badge" style="left:86px" width="78" height="34" viewBox="0 0 78 34"><rect width="78" height="34" fill="var(--seal)"/></svg>
<svg class="abs badge" style="left:290px" width="30" height="30" viewBox="0 0 30 30"><rect width="30" height="30" fill="var(--seal)"/></svg>
<svg class="abs badge" style="left:510px;top:912px" width="46" height="46" viewBox="0 0 46 46"><circle cx="23" cy="23" r="23" fill="var(--seal)"/></svg>
<svg class="abs badge" style="left:700px" width="95" height="30" viewBox="0 0 95 30"><rect width="95" height="30" fill="var(--seal)"/></svg>

<footer class="abs footer"></footer>
<div class="abs fcol" style="left:98px"><h4>About Us</h4><ul><li>History</li><li>Expertize</li><li>Identify</li><li>Strategy</li><li>Contact Us</li></ul></div>
<div class="abs fcol" style="left:216px"><h4>Investment</h4><ul><li>Term Deposits</li><li>Management &amp; Strategy</li><li>Client Relations</li><li>Financial Privacy</li><li>Tax Advice</li><li>Wealth Analysis &amp; Financial Planning</li><li>Active Advisory Group</li><li>Active Advisory Group</li><li>Manager Selection Services</li><li>Private Equity</li></ul></div>
<div class="abs fcol" style="left:414px"><h4>Funds</h4><ul><li>Overview</li><li>Administration</li><li>Funds Security</li><li>Core Services</li><li>Reporting</li><li>Revenue Opportunities</li><li>How it works?</li><li>Glossary</li></ul></div>
<div class="abs fcol" style="left:555px"><h4>Currency Exchange</h4><ul><li>Foreign Exchange</li><li>Fx Forward</li><li>Fx Options</li></ul></div>
<div class="abs fcol" style="left:555px;top:1079px"><h4>Account</h4><ul><li>Apply Now</li><li>Private Access</li></ul></div>
<div class="abs fcol" style="left:717px"><h4>Brokerage</h4><ul><li>Institutional</li><li>Research</li><li>Trading</li></ul></div>
<div class="abs footer-bottom">© Copyrights 2013 All rights Reserved</div>
</body>
</html>
```